Guiding Your Revenue Overhaul *

Bold eye-catching design for business non-fiction: I am seeking a bold, and clean design for a book. The book will be 6X9 for both the ebook and in print. I am open to ideas, but found that books like “steady as rain” with contrast are highly desirable for business books.

I am open to color choices.

I would also like a growth orientated graphic in the book - something to show growth, leadership, movement. Not just a plain graphic.

The title:

Guiding Your Revenue Overhaul

The subtitle - I am open to suggestions. Two subtitles I am considering:

A framework for new sales leaders and those who want to keep winning.

A guide for new sales leaders and those who want to keep winning.

The below is an introduction of the book: (Back Jacket)

Sales transformation is a topic that is infrequently written about. For the new sales leader, there are a myriad of books written on coaching, leadership, forecasting, solution selling and sales process but very little is written about how to assess a sales team and build a plan for long-term success.

Through my sales leadership career, whether recently promoted or starting with a new team, I have often asked the question: Where do I start?

In the end, I was disappointed with the answers from currently available books and research, left to figure it out myself - which I did over a decade, with great pain and through many transformations. The inability to answer the question – Where do I start? – is why I wrote this book. To answer that question.

The goal of this book is to help sales leaders answer that question by providing a framework to understand the business, build a plan, and guide the team through the different stages of a sales transformation. A framework to succeed at the fastest pace possible, quarter after quarter.

(End back jacket - the rest is just additional context)

Over the last decade, I have had the privilege of leading teams in North America, Europe, and Asia. I have led turnarounds, growth businesses, and realignments. Each team was different in size, complexity, and culture; and each one offered up new and unique challenges. Each team operated with different market dynamics: one was a commodity; one was a low-cost leader; one was a market innovator. Each transformation helped me learn by taking risks, by failing and by succeeding. At each step, I had many teachers; and as I learned, I made notes. Over time I built a framework that you can leverage as you read and absorb this book. As you lead your team through a sales transformation.

I hope that this book will become for you what The Copper Lantern is for me: a favorite on your bookshelf; underlined, highlighted, dog-eared, and an ongoing reference.

Sales leadership is a journey. It is never linear, and it is always changing. At different times, different parts of this book will apply, while others will not, but hopefully, you will find it a useful and long-lasting reference.

Target Market(s)

Business readers. Sales leaders.

Requirements
Must have
• Modern, clear, eye catching colours. Clean. Graphics that indicate growth, leadership, strength.
• Please ensure the design has the full cover and back jacket design. Please use the introduction of the book as the back jacket text.

```html
<!DOCTYPE html>
<html lang="en">
<head>
<meta charset="utf-8">
<title>Guiding Your Revenue Overhaul – Cover Spread</title>
<link href="https://fonts.googleapis.com/css2?family=Tinos:wght@400;700&display=swap" rel="stylesheet">
<style>
  :root {
    --canvas: #ffffff;
    --jacket: #f3f3f3;
    --ink: #111111;
    --body-ink: #222222;
    --accent: #e8414f;
    --photo-light: #f4f4f4;
    --photo-mid: #e6e6e6;
  }
  * { margin: 0; padding: 0; box-sizing: border-box; }
  html, body {
    width: 1200px; height: 1200px; overflow: hidden;
    background: var(--canvas);
    font-family: "Tinos", "Times New Roman", serif;
  }
  .spread {
    position: absolute; left: 0; top: 322px;
    width: 1200px; height: 554px;
    background: linear-gradient(90deg, var(--jacket) 0%, #f6f6f6 70%, #f1f1f1 100%);
  }
  .flap-text {
    position: absolute; left: 18px; top: 28px; width: 190px;
    font-size: 9px; line-height: 15px; color: var(--body-ink);
    text-align: justify; hyphens: auto;
  }
  .flap-text p + p { margin-top: 15px; }

  .back-cover { position: absolute; left: 246px; top: 28px; width: 319px; }
  .back-title {
    font-size: 16.5px; font-weight: 400; letter-spacing: 0.3px;
    white-space: nowrap; margin-bottom: 19px;
  }
  .back-blurb {
    font-size: 9px; line-height: 15px; color: var(--body-ink);
    text-align: justify;
  }
  .back-blurb p + p { margin-top: 15px; }

  .accent { color: var(--accent); }
  .dark { color: var(--ink); }

  .spine-title, .spine-author {
    position: absolute; writing-mode: vertical-rl;
    font-size: 15.5px; white-space: nowrap; letter-spacing: 0.3px;
  }
  .spine-title { left: 589px; top: 54px; }
  .spine-author { left: 589px; top: 408px; font-size: 12.5px; color: var(--ink); }

  .front-cover { position: absolute; left: 616px; top: 0; width: 360px; text-align: center; }
  .title { font-weight: 400; line-height: 1; }
  .title span { display: block; white-space: nowrap; }
  .title .line-1 { font-size: 72px; margin-top: 30px; color: var(--accent); }
  .title .line-2 { font-size: 50px; margin-top: 16px; color: var(--ink); }
  .title .line-3 { font-size: 58px; margin-top: 14px; color: var(--accent); }
  .subtitle {
    font-size: 20px; line-height: 19px; color: var(--ink);
    margin-top: 18px; white-space: nowrap;
  }
  .cover-image {
    position: absolute; left: 0; top: 294px; width: 360px; height: 192px;
    background: radial-gradient(ellipse at 50% 55%, var(--photo-mid) 0%, var(--photo-light) 70%, transparent 100%);
  }
  .author {
    position: absolute; left: 0; top: 497px; width: 360px;
    font-size: 26px; color: var(--ink); letter-spacing: 0.3px;
  }
</style>
</head>
<body>
  <section class="spread">
    <div class="flap-text">
      <p>Over the last decade, I have had the privilege of leading teams in North America, Europe, and Asia. I have led turnarounds, growth businesses, and realignments. Each team was different in size, complexity, and culture; and each one offered up new and unique challenges. Each team operated with different market dynamics: one was a commodity; one was a low-cost leader; one was a market innovator. Each transformation helped me learn by taking risks, by failing and by succeeding. At each step, I had many teachers; and as I learned, I made notes. Over time I built a framework that you can leverage as you read and absorb this book. As you lead your team through a sales transformation.</p>
      <p>I hope that this book will become for you what The Copper Lantern is for me: a favorite on your bookshelf; underlined, highlighted, dog-eared, and an ongoing reference.</p>
      <p>Sales leadership is a journey. It is never linear, and it is always changing. At different times, different parts of this book will apply, while others will not, but hopefully, you will find it a useful and long-lasting reference.</p>
    </div>

    <div class="back-cover">
      <h2 class="back-title"><span class="accent">GUIDING</span> <span class="dark">YOUR REVENUE</span> <span class="accent">OVERHAUL</span></h2>
      <div class="back-blurb">
        <p>Sales transformation is a topic that is infrequently written about. For the new sales leader, there are a myriad of books written on coaching, leadership, forecasting, solution selling and sales process but very little is written about how to assess a sales team and build a plan for long-term success.</p>
        <p>Through my sales leadership career, whether recently promoted or starting with a new team, I have often asked the question: Where do I start?</p>
        <p>In the end, I was disappointed with the answers from currently available books and research, left to figure it out myself - which I did over a decade, with great pain and through many transformations. The inability to answer the question – Where do I start? – is why I wrote this book. To answer that question.</p>
        <p>The goal of this book is to help sales leaders answer that question by providing a framework to understand the business, build a plan, and guide the team through the different stages of a sales transformation. A framework to succeed at the fastest pace possible, quarter after quarter.</p>
      </div>
    </div>

    <div class="spine-title"><span class="accent">GUIDING</span> <span class="dark">YOUR REVENUE</span> <span class="accent">OVERHAUL</span></div>
    <div class="spine-author">AUTHOR NAME</div>

    <div class="front-cover">
      <h1 class="title">
        <span class="line-1">GUIDING</span>
        <span class="line-2">YOUR REVENUE</span>
        <span class="line-3">OVERHAUL</span>
      </h1>
      <p class="subtitle">A guide for new sales leaders and those<br>who want to keep winning</p>
      <div class="cover-image" role="img" aria-label="Soft-focus photo of coloured game pawns on white, a red pawn leading in front"></div>
      <p class="author">AUTHOR NAME</p>
    </div>
  </section>
</body>
</html>
```